Redesign of existing Web Design Project

I wish to redsesign the web pages on www.bqrl.com.au

Background of Halvern Oakridge

Halvern Oakridge Construction Services was established in 2004 as a boutique construction company offering construction advice and management services. We assist people in the construction minefield – step by step.

We offer services in: -

• Construction Management
• Project Management
• Building

The essence of our business is ensuring every project we undertake achieves the client’s objectives. Our experience has shown the secrets to a profitable project are -

• Planning
• Attention to detail
• Value add

We take the trouble to understand the client’s needs in person. Our hands-on approach ensures those involved deliver to the required quality standards at the scheduled times.

Our area of works include: -

• Residential single and multistorey developments
• Education facilities
• Suburban commercial building and refurbishment
• Health
• Defence
• Industrial

Objective of Acquisition

We are planning to expand our business activities. We are aiming to increase our turnover and use website as an increased passive selling tool.

Possible company type

This is an ideal opportunity for person who can capture readers attention.

Target Market(s)

see www.bqrl.com.au

Industry/Entity Type

Construction

Requirements
Must have
• Capture peoples attention on readers zones

```html
<!DOCTYPE html>
<html lang="en">
<head>
<meta charset="utf-8">
<title>Halvern Oakridge Construction Services</title>
<link href="https://fonts.googleapis.com/css2?family=Arimo:wght@400;700&display=swap" rel="stylesheet">
<style>
  :root {
    --bg: #f6f6f8;
    --ink: #2b3a44;
    --muted: #9aa3a8;
    --rule: #2d5470;
    --brand: #3f5d8c;
    --teal: #3d6670;
    --nav: #1f2d3d;
    --foot: #666b70;
    --link: #0f2a50;
  }
  * { margin: 0; padding: 0; box-sizing: border-box; }
  html, body { width: 1200px; height: 769px; overflow: hidden; background: var(--bg); }
  body { position: relative; font-family: "Arimo", Arial, sans-serif; color: var(--ink); }

  .hero { position: absolute; left: 0; top: 0; width: 1200px; height: 545px; }

  .service {
    position: absolute; font-size: 15px; letter-spacing: -0.2px;
    padding-left: 16px; padding-bottom: 4px; border-bottom: 1px solid var(--rule);
  }
  .service::before {
    content: ""; position: absolute; left: 0; top: 6px;
    width: 7px; height: 7px; border-radius: 50%; background: var(--ink);
  }
  .service strong { font-weight: 700; color: var(--ink); }
  .service span { color: var(--muted); }
  .service--building { left: 352px; top: 156px; width: 211px; }
  .service--management { left: 714px; top: 321px; width: 297px; padding-left: 116px; }
  .service--management::before { left: 116px; }
  .service--management { text-indent: 16px; }
  .service--project { left: 177px; top: 463px; width: 241px; }

  .brand { position: absolute; left: 0; top: 556px; width: 1200px; text-align: center; }
  .brand__name { font-size: 26px; font-weight: 700; color: var(--brand); letter-spacing: 0.2px; line-height: 1; }
  .brand__tag { margin-top: 7px; font-size: 14px; color: var(--teal); }

  .main-nav { position: absolute; left: 0; top: 629px; width: 1200px; text-align: center; font-size: 12px; color: var(--nav); }
  .main-nav a { color: var(--nav); text-decoration: none; }
  .main-nav .sep { margin: 0 9px; }

  .site-footer { position: absolute; left: 0; top: 663px; width: 1200px; text-align: center; font-size: 10.5px; color: var(--foot); }
  .site-footer a { color: var(--foot); text-decoration: none; }
  .site-footer .owner { color: var(--link); }
  .site-footer .sep { margin: 0 11px; }
</style>
</head>
<body>
  <section class="hero">
    <svg width="1200" height="545" viewBox="0 0 1200 545">
      <defs>
        <radialGradient id="groundShade" cx="0.5" cy="0.5" r="0.5">
          <stop offset="0" stop-color="#9ea2a6" stop-opacity="0.7"/>
          <stop offset="1" stop-color="#9ea2a6" stop-opacity="0"/>
        </radialGradient>
        <linearGradient id="sceneTone" x1="0" y1="0" x2="0.6" y2="1">
          <stop offset="0" stop-color="#c9dde4"/>
          <stop offset="0.35" stop-color="#4a8aa8"/>
          <stop offset="0.6" stop-color="#8a9aa0"/>
          <stop offset="0.8" stop-color="#a08670"/>
          <stop offset="1" stop-color="#c9c4bc"/>
        </linearGradient>
      </defs>
      <ellipse cx="611" cy="538" rx="320" ry="8" fill="url(#groundShade)"/>
      <polygon role="img" aria-label="Triangular photo montage of glass office towers, a crane, a modern building entrance and site engineers" points="616,68 336,540 879,540" fill="url(#sceneTone)"/>
    </svg>

    <div class="service service--building"><strong>Building</strong><span>Construction</span></div>
    <div class="service service--management"><strong>Construction</strong><span>Management</span></div>
    <div class="service service--project"><strong>Project</strong><span>Management</span></div>
  </section>

  <header class="brand">
    <div class="brand__name">HALVERN OAKRIDGE</div>
    <div class="brand__tag">Construction Services</div>
  </header>

  <nav class="main-nav">
    <a href="#">Home</a><span class="sep">|</span>
    <a href="#">About Us</a><span class="sep">|</span>
    <a href="#">Building</a><span class="sep">|</span>
    <a href="#">Construction Management</a><span class="sep">|</span>
    <a href="#">Project Management</a><span class="sep">|</span>
    <a href="#">Links</a><span class="sep">|</span>
    <a href="#">Free Downloads</a><span class="sep">|</span>
    <a href="#">Careers</a><span class="sep">|</span>
    <a href="#">Contacts</a>
  </nav>

  <footer class="site-footer">
    Copyright © 2008 <a class="owner" href="#">Halvern Oakridge</a>, All Rights Reserved - Webmaster<span class="sep">|</span><a href="#">Privacy policy</a><span class="sep">|</span><a href="#">Admint</a>
  </footer>
</body>
</html>
```